the halvorsen group premier division

design a DL A4 tri fold brochure to reflect our creative landscape business
my web site www.thehalvorsengroup.com.au
has all the information needed
i will also be updating the website to be more updated and creative design

```html
<!DOCTYPE html>
<html lang="en">
<head>
<meta charset="utf-8">
<title>The Halvorsen Group – Creative Landscape Brochure</title>
<link href="https://fonts.googleapis.com/css2?family=Montserrat:wght@400;500;600;700&display=swap" rel="stylesheet">
<style>
:root{
  --cyan:#29b6e8;
  --orange:#f0901e;
  --ink:#2b2b2d;
  --charcoal:#3a3a3c;
  --grey:#5b5b5e;
  --paper:#ffffff;
  --stage:#e6e6e8;
  --text:#3d3d3f;
}
*{box-sizing:border-box;margin:0;padding:0}
html,body{width:1200px;height:800px;overflow:hidden}
body{background:var(--stage);font-family:'Montserrat',sans-serif;color:var(--text);position:relative}
.spread{position:absolute;left:16px;top:96px;width:860px;height:608px;background:var(--paper);overflow:hidden;box-shadow:0 2px 8px rgba(0,0,0,.15)}
.panel{position:absolute;top:0;height:608px;width:286.67px}
.panel--one{left:0}
.panel--two{left:286.67px;background:var(--charcoal)}
.panel--three{left:573.33px}
.heading{font-weight:700;line-height:1;font-size:17px;color:var(--ink)}
.heading .accent-cyan{color:var(--cyan);display:block}
.heading .accent-orange{color:var(--orange);display:block}
.copy{font-size:8px;line-height:1.35;font-weight:500}
.copy p{margin-bottom:6px}
.photo{position:absolute}
.photo--house{left:140px;top:18px;width:250px;height:150px;border-radius:30px 70px 30px 70px;background:linear-gradient(160deg,#9fc6e8 0%,#e9ede8 45%,#1c6fb8 80%,#0f3f6f 100%);border:3px solid #fff}
.consult-title{position:absolute;left:18px;top:16px}
.consult-copy{position:absolute;left:18px;top:54px;width:118px}
.consult-copy-wide{position:absolute;left:18px;top:176px;width:255px}
.earth-title{position:absolute;left:70px;top:346px}
.earth-copy{position:absolute;left:70px;top:386px;width:205px;text-align:justify;line-height:1.3}
.earth-copy p{margin-bottom:4px}
.corner-band{position:absolute;left:0;bottom:0;width:60px;height:120px;background:var(--grey);border-top-right-radius:60px}
.streak{position:absolute;left:115px;top:20px;width:70px;height:60px;border-radius:30px 8px 30px 8px;background:linear-gradient(135deg,#35c3c9,#a8d85a)}
.streak--low{left:10px;top:420px;width:50px;height:60px}
.maint-title{position:absolute;left:40px;top:132px;width:220px;text-align:right;color:#fff}
.maint-title .accent-cyan{color:var(--cyan)}
.maint-copy{position:absolute;left:30px;top:180px;width:235px;color:#fff;text-align:right}
.photo--site{left:320px;top:390px;width:270px;height:200px;border-radius:80px 30px 80px 30px;background:linear-gradient(180deg,#a9c3df 0%,#c9d4df 40%,#4a3b32 70%,#2b241f 100%);border:4px solid #fff}
.install-title{position:absolute;left:24px;top:16px}
.install-copy{position:absolute;left:24px;top:54px;width:245px}
.list-cols{position:absolute;left:24px;top:118px;width:245px;display:flex;gap:10px}
.bullets{list-style:none;font-size:8px;font-weight:500;line-height:1.45;flex:1}
.bullets li{display:flex;align-items:flex-start;gap:5px}
.bullets li::before{content:"";flex:none;width:6px;height:6px;margin-top:3px;background:var(--cyan)}
.bullets li.alt::before{background:var(--orange)}
.brand-mark{position:absolute;left:24px;top:262px;display:flex;align-items:center;gap:8px}
.brand-square{width:34px;height:34px;border-radius:8px;background:var(--cyan)}
.brand-name{font-size:13px;font-weight:700;color:var(--ink);line-height:1.15}
.materials{position:absolute;left:24px;top:360px;width:245px;text-align:right}
.materials .heading{font-size:14px}
.materials .lead{font-size:10px;font-weight:600;margin-top:3px}
.materials .bullets{margin-top:10px;display:grid;grid-template-columns:1fr 1fr;text-align:left;font-size:9px}
.cover{position:absolute;left:900px;top:96px;width:287px;height:608px;background:var(--paper);overflow:hidden;box-shadow:0 2px 8px rgba(0,0,0,.15)}
.photo--garden{left:0;top:0;width:287px;height:270px;border-bottom-left-radius:120px;background:linear-gradient(170deg,#6b8f4a 0%,#a7b89a 40%,#6d5a46 75%,#4a3a2c 100%)}
.cover-tile{position:absolute;right:-10px;top:180px;width:80px;height:80px;border-radius:18px;background:var(--orange);transform:rotate(45deg)}
.cover-title{position:absolute;left:26px;top:330px;width:240px;text-align:right}
.cover-title .line-creative{font-size:24px;font-weight:700;color:var(--cyan)}
.cover-title .line-landscape{font-size:38px;font-weight:700;color:var(--orange);line-height:1}
.cover-title .line-sub{font-size:14px;font-weight:600;color:var(--ink)}
.cover-brand{position:absolute;left:0;top:470px;width:287px;display:flex;flex-direction:column;align-items:center;gap:10px}
.cover-brand .brand-square{width:40px;height:40px}
.cover-brand .brand-name{font-size:17px;text-align:center}
</style>
</head>
<body>
<main class="spread" aria-label="Brochure inside spread">
  <section class="panel panel--one">
    <h2 class="heading consult-title"><span class="accent-cyan">Consultation</span>and Design</h2>
    <div class="copy consult-copy"><p>The Halvorsen Group can work with you for a full landscape design concept or visit your site to discuss an existing plan.</p></div>
    <div class="copy consult-copy-wide">
      <p>Our landscape designers will begin by discussing your needs and look at your property and setting to create a concept where all attributes are considered from the land itself, design style, the elements and impact, through to lifestyle, and functionality and of course budget.</p>
      <p>Whether it be new or existing, Tom Ashby can provide advice on materials, earth and irrigation, planting, features and so with only quality and longevity in mind.</p>
      <p>You may also opt for a digital interpretation of your design, at an additional cost, to help you visualise the transformation and how the design fits in with its surrounds.</p>
      <p>If you have something particular in mind or uncertain about, Tom would be happy to assist.</p>
    </div>
    <h2 class="heading earth-title"><span class="accent-orange">Earthwork</span>&amp; Site Preparation</h2>
    <div class="copy earth-copy">
      <p>Depending on the nature of the site, it is imperative that your foundation and earth is well prepared for construction and planting. This will determine a quality outcome and the longevity we promote so you don't have issues in the future.</p>
      <p>The Halvorsen group provides the relevant services required so your ground can be covered!</p>
      <p>This includes, clearing, excavation, levelling, solid foundations and so on. With experience in soft and hard landscape installation and construction, we know that longevity is impacted by solid preparations.</p>
      <p>The Halvorsen group manages all excavation and site preparation works for you.</p>
    </div>
    <div class="corner-band"></div>
  </section>
  <section class="panel panel--two">
    <div class="streak" role="img" aria-label="Colourful paint streak decoration"></div>
    <h2 class="heading maint-title">Maintenance<span class="accent-cyan">Programs</span></h2>
    <div class="copy maint-copy">
      <p>We understand people can be 'caught up' or procrastinate in attending to landscape maintenance.</p>
      <p>Once you have invested in an outdoor project, it's important it is retained for continuous enjoyment and longevity, and to avoid any costly neglect!</p>
      <p>As an option, The Halvorsen group can set a maintenance program according to your landscape needs addressing various landscaping elements including decking, trees and plants, lighting and so forth.</p>
    </div>
    <div class="streak streak--low" role="img" aria-label="Colourful paint streak decoration"></div>
  </section>
  <div class="photo photo--house" role="img" aria-label="Photo of a modern home with a lit swimming pool at dusk"></div>
  <div class="photo photo--site" role="img" aria-label="Photo of a construction site with a house and a work vehicle"></div>
  <section class="panel panel--three">
    <h2 class="heading install-title"><span class="accent-orange">Installation</span>&amp; Construction</h2>
    <div class="copy install-copy"><p>Upon a well prepared site, The Halvorsen group are a professional landscape and construction company that works with a whole range of materials and structural designs. Browse through our portfolio to see our quality finishes and versatile capabilities including:</p></div>
    <div class="list-cols">
      <ul class="bullets">
        <li>Decking</li><li>Tiling</li><li>Paving</li><li>Pathways</li><li>Walls and Screening</li><li>Irrigation</li><li>Plant supply &amp; installation</li><li class="alt">Lawn</li>
      </ul>
      <ul class="bullets">
        <li>Covered Structures &amp; Arbours</li><li>Water Features</li><li>Rock Features</li><li>Lighting</li><li>Irrigation and Automatic Systems</li><li class="alt">Concreting</li><li class="alt">Aggregate designs</li><li class="alt">Pool Paving and Features</li><li>Metal Sculptures</li>
      </ul>
    </div>
    <div class="brand-mark"><span class="brand-square"></span><span class="brand-name">The Halvorsen Group</span></div>
    <div class="materials">
      <h3 class="heading"><span class="accent-cyan">Just Some</span>Of The Materials</h3>
      <p class="lead">We Have Worked With Include</p>
      <ul class="bullets">
        <li>Bluestone</li><li>Hardwood</li><li class="alt">Limestone</li><li class="alt">Aggregate</li>
      </ul>
    </div>
  </section>
</main>
<section class="cover" aria-label="Brochure front cover">
  <div class="photo photo--garden" role="img" aria-label="Photo of a landscaped garden with stepping stones, timber deck and white outdoor chairs"></div>
  <div class="cover-tile"></div>
  <h1 class="cover-title">
    <span class="line-creative">Creative</span><br>
    <span class="line-landscape">Landscape</span><br>
    <span class="line-sub">Design &amp; Construction</span>
  </h1>
  <div class="cover-brand">
    <span class="brand-square"></span>
    <span class="brand-name">The Halvorsen Group<br>Premier Division</span>
  </div>
</section>
</body>
</html>
```